House-share and Room Rental Website (With Focus on the Bedroom Landing Page)

Looking for website design for our House-share (executive accommodation) and room rental business.

Our company name is: Quellnest could also be written as QuellNest or quellnest. Either is fine .. just looking for a nice clean catchy logo to go with the design.

EXAMPLES
These are examples of other websites in this field that are doing well. this is a kind of baseline.
https://dovelinter.example.au/
https://www.kestrib.example/
https://www.velunor.example/
https://www.trisbel.example/
https://www.pondmarrowseek.example.au/

Our business model is to rent rooms to people looking for high-quality accommodation. We fill the gap between those looking to rent rooms and those with rooms to rent. However, our model is slightly different from those already on the market as we looking to fill a massive gap in the market delivering upmarket rooms for rent.(Executive Accommodation) also in the back end will be coupled with a self management process in the back end.

We offer executive style accommodation that stands out above the rest. With special extras like fire safety.. and management processes that create happier homes. We are looking for a web design package that can help us grow and scale our business. We need a design that is captivating

Our MAIN focus is having a room landing page that stands out from the rest... The core of our business will rely on the promotion of the rooms in a share house... so the whole design relies on the BEDROOM landing page to drive results.

Target Market(s)

We have 2 markets we are aiming at ... the first market is people offering rooms to rent who want the highest rental return. The second market is people looking to rent safe, high-quality rooms, in houses that are well managed and looked after.

Industry/Entity Type

Share Economy

Logo Text

QuellNest

Number of Pages Required

5+ page

Font styles to use
Sans Serif

Colors
3276b5

Requirements
Must have
• A messaging system whereby we can create direct communication between those offering rooms and those looking for rooms.
• A call to action that says " Schedule an Inspection"
• Landing page for promoting rooms
• A home page for showing stock.
• Profile page for those selling rooms
• Profile page for those looking for rooms.
• A scheduling calendar for booking inspections
Nice to have
• Pages where new residents can lock in a room.. pay bond and rents.. and sign contracts
• Notifications
• SMS capabilities in the backend.
Should not have
• No script or handwriting fonts.

```html
<!DOCTYPE html>
<html lang="en">
<head>
<meta charset="utf-8">
<title>QuellNest – Master Bedroom</title>
<link rel="stylesheet" href="https://fonts.googleapis.com/css2?family=Josefin+Sans:wght@300;400;600;700&family=Montserrat:wght@400;600;700&family=Arimo:wght@400;700&display=swap">
<style>
:root{
  --blue:#3276b5;
  --blue-dark:#2a67a0;
  --ink:#333333;
  --grey:#7a7a7a;
  --line:#d9d9d9;
  --footer:#2f2f2f;
  --footer-deep:#242424;
  --footer-text:#a9a9a9;
  --white:#ffffff;
}
*{box-sizing:border-box;margin:0;padding:0}
html,body{width:1200px;height:3509px;overflow:hidden}
body{position:relative;background:var(--white);font-family:"Josefin Sans",sans-serif;color:var(--ink)}
.abs{position:absolute}

/* top bar */
.topbar{top:0;left:0;width:1200px;height:38px;font-family:"Montserrat",sans-serif;font-size:11px;color:var(--grey)}
.topbar .contact{position:absolute;top:12px;display:flex;align-items:center;gap:8px}
.topbar .contact svg{width:12px;height:12px}
.social-dot{position:absolute;top:11px;width:14px;height:14px;border-radius:50%;background:var(--blue)}

/* nav */
.nav{top:38px;left:0;width:1200px;height:72px;background:var(--blue);color:var(--white)}
.brand{position:absolute;left:110px;top:18px;display:flex;align-items:center;gap:14px}
.brand .mark{width:36px;height:36px;border-radius:50%;background:var(--white)}
.brand .name{font-family:"Montserrat",sans-serif;font-weight:700;font-size:24px;letter-spacing:.5px}
.menu{position:absolute;top:29px;font-family:"Montserrat",sans-serif;font-weight:600;font-size:11.5px;letter-spacing:.3px}

/* media */
.hero{top:110px;left:0;width:1200px;height:503px;background:linear-gradient(180deg,#4a3c34 0%,#7a6555 45%,#c9b8a4 70%,#5a4a3f 100%)}
.thumb{top:636px;width:150px;height:120px}
.arrow{top:680px;width:30px;height:30px;border:2px solid var(--blue);border-radius:50%;display:flex;align-items:center;justify-content:center}

/* overview */
.h-section{font-family:"Josefin Sans",sans-serif;font-weight:600;letter-spacing:.5px;color:#2b2b2b}
.overview-title{left:105px;top:836px;font-size:38px}
.overview-rule{left:105px;top:884px;width:180px;height:1px;background:#9a9a9a}
.overview-copy{left:105px;top:916px;width:430px;font-size:17px;line-height:44.6px;color:#555;font-weight:400}
.features{left:105px;top:1254px;list-style:none;font-size:19px;color:#444}
.features li{height:44.6px;display:flex;align-items:center;gap:14px}
.features b{font-weight:700;color:#222}
.features svg{width:18px;height:18px;flex:none}
.transport-title{left:112px;top:1741px;font-size:25px;font-weight:600}
.transport-icons{left:112px;top:1808px;display:flex;gap:34px}
.transport-icons svg{width:52px;height:52px}
.distance{left:114px;top:1894px;font-size:21px;color:#444}
.distance b{font-weight:700;color:#222}
.divider{left:601px;top:824px;width:1px;height:1166px;background:var(--line)}

/* room card */
.room-title{left:676px;top:836px;font-size:32px;font-weight:700;color:var(--blue);letter-spacing:.5px}
.room-address{left:676px;top:890px;font-size:28px;line-height:38px;color:#8a8a8a;font-weight:400}
.utilities{left:676px;top:1000px;font-size:23px;color:#444}
.utilities b{font-weight:700;color:#222}
.price{left:676px;top:1068px;font-size:19px;color:#555;display:flex;align-items:baseline;gap:10px}
.price .amount{font-size:42px;font-weight:700;color:var(--blue)}
.price-rule{left:676px;top:1148px;width:428px;height:2px;background:#bdbdbd}
.btn{top:1193px;height:59px;display:flex;align-items:center;justify-content:center;gap:18px;font-size:20px;font-weight:700;letter-spacing:1px}
.btn-outline{left:679px;width:191px;border:2px solid var(--blue);color:#333}
.btn-solid{left:906px;width:189px;background:var(--blue);color:var(--white)}
.schedule-title{left:703px;top:1341px;font-size:26px;font-weight:600}

/* calendar */
.calendar{left:707px;top:1404px;width:318px;height:246px;background:var(--white);box-shadow:0 6px 22px rgba(0,0,0,.18);padding:24px 26px}
.cal-grid{display:grid;grid-template-columns:repeat(7,1fr);row-gap:10px;text-align:center;font-family:"Arimo",sans-serif;font-size:12px;color:#666}
.cal-grid .wd{font-size:8px;color:#aaa;letter-spacing:.3px}
.cal-grid .wd.sat{color:#333;font-weight:700;border-bottom:2px solid #e05a4f}
.cal-grid span{position:relative;height:25px;line-height:25px}
.cal-grid .today{background:var(--blue);color:var(--white);border-radius:50%;width:25px;margin:0 auto;font-weight:700}
.cal-grid .busy::after{content:"";position:absolute;left:50%;bottom:-1px;width:4px;height:4px;margin-left:-2px;border-radius:50%;background:#e05a4f}

.message{left:672px;top:1729px;width:425px;height:157px;border:2px solid #bcbcbc;padding:28px 42px;font-size:18px;color:#9a9a9a}
.send{left:672px;top:1926px;width:425px;height:54px;background:var(--blue);color:var(--white);font-size:21px;font-weight:700;letter-spacing:2px;display:flex;align-items:center;justify-content:center}

/* amenities */
.center-title{left:0;width:1200px;text-align:center;font-size:38px}
.center-rule{left:530px;width:140px;height:1px;background:#9a9a9a}
.amenity{top:2218px;width:150px;text-align:center;font-size:19px;line-height:37px;color:#333}
.amenity svg{width:58px;height:58px;margin-bottom:24px}

/* map */
.map{top:2593px;left:0;width:1200px;height:384px;background:linear-gradient(135deg,#d9dfe3 0%,#eaece6 40%,#e4e2d6 60%,#d2dde5 100%)}

/* tweet band */
.tweet{top:2977px;left:0;width:1200px;height:103px;background:var(--blue);color:var(--white)}
.tweet .dot{position:absolute;left:196px;top:34px;width:34px;height:34px;border-radius:50%;background:var(--white)}
.tweet p{position:absolute;left:300px;width:680px;top:30px;text-align:center;font-family:"Arimo",sans-serif;font-weight:700;font-size:13px;line-height:28px}

/* footer */
.footer{top:3080px;left:0;width:1200px;height:372px;background:var(--footer);font-family:"Arimo",sans-serif;color:var(--footer-text);font-size:11px}
.footer h4{position:absolute;top:74px;color:var(--white);font-size:12px;font-weight:700;letter-spacing:.3px}
.news{position:absolute;left:110px;display:flex;gap:14px}
.news .pic{width:47px;height:47px;background:linear-gradient(135deg,#8fa4b8,#d6c7b4)}
.news b{display:block;color:var(--white);font-size:11px;line-height:15px;width:170px}
.news small{display:block;font-size:9px;color:#888;margin-top:3px}
.links{position:absolute;top:114px;list-style:none;line-height:30.5px}
.links .on{color:var(--white);font-weight:700}
.mail-copy{position:absolute;left:611px;top:114px;width:210px;line-height:18px}
.mail-field{position:absolute;left:611px;top:162px;width:190px;height:28px;background:var(--white);color:#aaa;font-size:10px;padding:8px 14px}
.mail-btn{position:absolute;left:807px;top:162px;width:28px;height:28px;background:var(--blue);display:flex;align-items:center;justify-content:center}
.privacy{position:absolute;left:611px;top:200px;font-size:9px;color:#888}
.foot-social{position:absolute;top:258px;width:22px;height:22px;border-radius:50%;background:#4a4a4a}
.foot-social.active{background:var(--blue);border-radius:0}
.finance{position:absolute;left:861px;top:114px;width:220px;line-height:18px}
.finance-row{position:absolute;left:861px;display:flex;gap:14px;line-height:18px}
.finance-row svg{width:12px;height:12px;margin-top:3px;flex:none}

.bottom{top:3452px;left:0;width:1200px;height:57px;background:var(--footer-deep);font-family:"Arimo",sans-serif;font-size:10px;color:#8c8c8c}
.bottom .copy{position:absolute;left:110px;top:22px}
.bottom .nav-links{position:absolute;right:132px;top:22px;display:flex;gap:22px}
</style>
</head>
<body>

<!-- top bar -->
<header>
<div class="abs topbar">
  <div class="contact" style="left:100px">
    <svg viewBox="0 0 12 12"><rect x="3" y="0.5" width="6" height="11" rx="1" fill="none" stroke="#3276b5" stroke-width="1.3"/></svg>
    <span>1234 - 5678 - 9012</span>
  </div>
  <div class="contact" style="left:262px">
    <svg viewBox="0 0 12 12"><rect x="0.5" y="2" width="11" height="8" fill="#3276b5"/><path d="M1 2.5 6 6.5 11 2.5" fill="none" stroke="#fff"/></svg>
    <span style="color:var(--blue)">support@quellnest.example</span>
  </div>
  <span class="social-dot" style="left:945px"></span>
  <span class="social-dot" style="left:1001px"></span>
  <span class="social-dot" style="left:1057px"></span>
</div>

<nav class="abs nav">
  <div class="brand"><span class="mark"></span><span class="name">QUELLNEST</span></div>
  <span class="menu" style="left:672px">HOME</span>
  <span class="menu" style="left:738px">ABOUT US</span>
  <span class="menu" style="left:830px">ROOMS</span>
  <span class="menu" style="left:904px">BOOK NOW</span>
  <span class="menu" style="left:1000px">CONTACT</span>
  <svg class="abs" style="left:1080px;top:28px" width="16" height="16" viewBox="0 0 16 16"><circle cx="6.5" cy="6.5" r="5" fill="none" stroke="#fff" stroke-width="2"/><path d="M10.5 10.5 15 15" stroke="#fff" stroke-width="2.4"/></svg>
</nav>
</header>

<main>
<div class="abs hero" role="img" aria-label="Photo of the master bedroom with a made double bed, bedside lamps and tall windows at dusk"></div>

<div class="abs arrow" style="left:50px"><svg width="12" height="12" viewBox="0 0 12 12"><path d="M8 2 4 6 8 10" fill="none" stroke="#3276b5" stroke-width="2"/></svg></div>
<div class="abs thumb" style="left:110px;background:linear-gradient(135deg,#d8d2c8,#a89a88)" role="img" aria-label="Living room photo"></div>
<div class="abs thumb" style="left:280px;background:linear-gradient(135deg,#5d4a35,#c8a878)" role="img" aria-label="Lounge with fireplace photo"></div>
<div class="abs thumb" style="left:450px;background:linear-gradient(135deg,#8a8580,#ded8cf)" role="img" aria-label="Sitting area photo"></div>
<div class="abs thumb" style="left:620px;background:linear-gradient(135deg,#3c4a4a,#6d7f7c)" role="img" aria-label="Dark green sofa room photo"></div>
<div class="abs thumb" style="left:790px;background:linear-gradient(135deg,#ece6dc,#b9ad9c)" role="img" aria-label="Bright lounge photo"></div>
<div class="abs thumb" style="left:940px;width:150px;background:linear-gradient(135deg,#2e3540,#c7ccd2)" role="img" aria-label="Dining room photo"></div>
<div class="abs arrow" style="left:1118px"><svg width="12" height="12" viewBox="0 0 12 12"><path d="M4 2 8 6 4 10" fill="none" stroke="#3276b5" stroke-width="2"/></svg></div>

<!-- overview -->
<h2 class="abs h-section overview-title">OVERVIEW</h2>
<div class="abs overview-rule"></div>
<p class="abs overview-copy">Sed ut perspiciatis unde omnis iste natus error sit voluptatem accusantium doloremque laudantium, totam rem aperiam, eaque ipsa quae ab illo inven-tore veritatis et quasi architecto beatae vitae dicta sunt explicabo. Nemo enim ipsam voluptatem quia voluptas sit aspernatur aut odit aut fugit, sed quia consequuntur magni dolores eos qui ratione</p>

<ul class="abs features">
  <li><svg viewBox="0 0 18 18"><circle cx="9" cy="9" r="7.5" fill="none" stroke="#3276b5" stroke-width="1.4"/><path d="M5 9.2 8 12 13.5 5.5" fill="none" stroke="#3276b5" stroke-width="1.6"/></svg>Gender Preference- <b>MALE</b></li>
  <li><svg viewBox="0 0 18 18"><circle cx="9" cy="9" r="7.5" fill="none" stroke="#3276b5" stroke-width="1.4"/><path d="M5 9.2 8 12 13.5 5.5" fill="none" stroke="#3276b5" stroke-width="1.6"/></svg>Size of room - <b>1000 Sqm</b></li>
  <li><svg viewBox="0 0 18 18"><circle cx="9" cy="9" r="7.5" fill="none" stroke="#3276b5" stroke-width="1.4"/><path d="M5 9.2 8 12 13.5 5.5" fill="none" stroke="#3276b5" stroke-width="1.6"/></svg>Bathroom - <b>SHARED</b></li>
  <li><svg viewBox="0 0 18 18"><circle cx="9" cy="9" r="7.5" fill="none" stroke="#3276b5" stroke-width="1.4"/><path d="M5 9.2 8 12 13.5 5.5" fill="none" stroke="#3276b5" stroke-width="1.6"/></svg>Parking - <b>STREET</b></li>
  <li><svg viewBox="0 0 18 18"><circle cx="9" cy="9" r="7.5" fill="none" stroke="#3276b5" stroke-width="1.4"/><path d="M5 9.2 8 12 13.5 5.5" fill="none" stroke="#3276b5" stroke-width="1.6"/></svg>Smoking - <b>ALLOWED</b></li>
  <li><svg viewBox="0 0 18 18"><circle cx="9" cy="9" r="7.5" fill="none" stroke="#3276b5" stroke-width="1.4"/><path d="M5 9.2 8 12 13.5 5.5" fill="none" stroke="#3276b5" stroke-width="1.6"/></svg>Minimum contract Year - <b>3 MONTHS</b></li>
  <li><svg viewBox="0 0 18 18"><circle cx="9" cy="9" r="7.5" fill="none" stroke="#3276b5" stroke-width="1.4"/><path d="M5 9.2 8 12 13.5 5.5" fill="none" stroke="#3276b5" stroke-width="1.6"/></svg>Bed size - <b>45' X 45'</b></li>
  <li><svg viewBox="0 0 18 18"><circle cx="9" cy="9" r="7.5" fill="none" stroke="#3276b5" stroke-width="1.4"/><path d="M5 9.2 8 12 13.5 5.5" fill="none" stroke="#3276b5" stroke-width="1.6"/></svg>Type of housemates - <b>PROFESSIONALS</b></li>
  <li><svg viewBox="0 0 18 18"><circle cx="9" cy="9" r="7.5" fill="none" stroke="#3276b5" stroke-width="1.4"/><path d="M5 9.2 8 12 13.5 5.5" fill="none" stroke="#3276b5" stroke-width="1.6"/></svg>Room type - <b>PRIVATE</b></li>
  <li><svg viewBox="0 0 18 18"><circle cx="9" cy="9" r="7.5" fill="none" stroke="#3276b5" stroke-width="1.4"/><path d="M5 9.2 8 12 13.5 5.5" fill="none" stroke="#3276b5" stroke-width="1.6"/></svg>Internet speed - <b>100 MBPS</b></li>
</ul>

<h3 class="abs h-section transport-title">TRANSPORT OPTIONS</h3>
<div class="abs transport-icons">
  <svg viewBox="0 0 52 52" fill="none" stroke="#3276b5" stroke-width="3"><rect x="10" y="6" width="32" height="36" rx="4"/><path d="M10 24h32M14 12h24"/><circle cx="17" cy="33" r="2.5" fill="#3276b5"/><circle cx="35" cy="33" r="2.5" fill="#3276b5"/><path d="M15 42v5M37 42v5M6 18v8M46 18v8"/></svg>
  <svg viewBox="0 0 52 52" fill="none" stroke="#3276b5" stroke-width="3"><rect x="13" y="6" width="26" height="32" rx="5"/><path d="M13 22h26"/><circle cx="20" cy="30" r="2" fill="#3276b5"/><circle cx="32" cy="30" r="2" fill="#3276b5"/><path d="M18 38 12 48M34 38 40 48M15 44h22"/></svg>
  <svg viewBox="0 0 52 52" fill="none" stroke="#3276b5" stroke-width="3"><path d="M8 34V26l5-10h26l5 10v8z"/><path d="M12 26h28"/><circle cx="16" cy="30" r="2" fill="#3276b5"/><circle cx="36" cy="30" r="2" fill="#3276b5"/><path d="M12 34v6M40 34v6"/></svg>
</div>
<p class="abs distance">Distance to the city &nbsp;- <b>3 KMS</b></p>

<div class="abs divider"></div>

<!-- room card -->
<h1 class="abs room-title">MASTER BEDROOM</h1>
<p class="abs room-address">418 Larkmoor Lane<br>Fenwick, VA 20987</p>
<p class="abs utilities">Utilites - &nbsp;<b>INCLUDED</b></p>
<p class="abs price"><span>From -</span><span class="amount">$270</span><span>/ Night</span></p>
<div class="abs price-rule"></div>
<div class="abs btn btn-outline">GALLERY
  <svg width="30" height="24" viewBox="0 0 30 24"><rect x="1" y="1" width="28" height="22" fill="none" stroke="#9a9a9a" stroke-width="2"/><path d="M4 20 12 11 18 17 22 13 27 20z" fill="#bdbdbd"/><circle cx="22" cy="7" r="2.5" fill="#bdbdbd"/></svg>
</div>
<div class="abs btn btn-solid">VIDEO
  <svg width="30" height="30" viewBox="0 0 30 30"><circle cx="15" cy="15" r="13" fill="none" stroke="#fff" stroke-width="2.4"/><path d="M13 9 19 15 13 21" fill="none" stroke="#fff" stroke-width="2.6"/></svg>
</div>

<h3 class="abs h-section schedule-title">SCHEDULE APPOINTMENT</h3>
<div class="abs calendar">
  <div class="cal-grid">
    <span class="wd">MON</span><span class="wd">TUE</span><span class="wd">WED</span><span class="wd">THU</span><span class="wd">FRI</span><span class="wd sat">SAT</span><span class="wd">SUN</span>
    <span></span><span></span><span>1</span><span>2</span><span>3</span><span>4</span><span>5</span>
    <span>6</span><span>7</span><span class="busy">8</span><span>9</span><span class="busy">10</span><span class="today">11</span><span>12</span>
    <span>13</span><span class="busy">14</span><span>15</span><span>16</span><span class="busy">17</span><span>18</span><span>19</span>
    <span>20</span><span>21</span><span>22</span><span>23</span><span>24</span><span class="busy">25</span><span>26</span>
    <span>27</span><span>28</span>
  </div>
</div>

<div class="abs message">Write a message to QuellNest</div>
<div class="abs send">SEND</div>

<!-- amenities -->
<h2 class="abs h-section center-title" style="top:2105px">ROOM AMENITIES</h2>
<div class="abs center-rule" style="top:2153px"></div>

<div class="abs amenity" style="left:42px">
  <svg viewBox="0 0 58 58" fill="none" stroke="#3276b5" stroke-width="2.4"><rect x="17" y="6" width="24" height="20" rx="3"/><path d="M12 30h34M17 30v8h24v-8M29 38v8M19 50l10-4 10 4M12 22v8M46 22v8"/></svg>
  <div>Furnished/<br>unfurnished</div>
</div>
<div class="abs amenity" style="left:201px">
  <svg viewBox="0 0 58 58" fill="none" stroke="#3276b5" stroke-width="2.4"><rect x="6" y="12" width="46" height="30"/><path d="M22 50h14M29 42v8"/></svg>
  <div>TV</div>
</div>
<div class="abs amenity" style="left:363px">
  <svg viewBox="0 0 58 58" fill="none" stroke="#3276b5" stroke-width="2.4"><rect x="12" y="6" width="34" height="44"/><path d="M12 30h34M29 6v24M25 18v4M33 18v4M26 38h6M14 50v4M44 50v4"/></svg>
  <div>Storage<br>space</div>
</div>
<div class="abs amenity" style="left:524px">
  <svg viewBox="0 0 58 58" fill="none" stroke="#3276b5" stroke-width="2.4"><rect x="14" y="6" width="24" height="16"/><path d="M26 22v6M4 28h50M6 28v24M52 28v24M36 28v24M36 38h16M42 33h4M42 44h4"/></svg>
  <div>Study Desk /<br>Workstation</div>
</div>
<div class="abs amenity" style="left:681px">
  <svg viewBox="0 0 58 58" fill="none" stroke="#3276b5" stroke-width="2.4"><rect x="15" y="4" width="28" height="48"/><path d="M15 28h28M29 4v24M26 14v4M32 14v4M21 36h16M21 44h16M18 52v3M40 52v3"/></svg>
  <div>Wardrobe</div>
</div>
<div class="abs amenity" style="left:842px">
  <svg viewBox="0 0 58 58" fill="none" stroke="#3276b5" stroke-width="2.4"><path d="M42 4v10h-6M20 22a16 10 0 0 1 32 0zM26 28v4M32 30v6M38 28v4M44 30v6M29 40v4M41 40v4M4 54h28M10 54v-8h16v8"/></svg>
  <div>Ensuite shower</div>
</div>
<div class="abs amenity" style="left:1001px">
  <svg viewBox="0 0 58 58" fill="none" stroke="#3276b5" stroke-width="2.4"><path d="M6 28h46M8 28v26h42V28M16 36h12v18M36 36h8M18 10a8 8 0 0 1 16 0h-16zM26 10V4M22 18h8v10M40 14h8v14"/></svg>
  <div>Kitchenette</div>
</div>

<!-- locations -->
<h2 class="abs h-section center-title" style="top:2479px">OUR LOCATIONS</h2>
<div class="abs center-rule" style="top:2528px"></div>
<div class="abs map" role="img" aria-label="Street map showing the locations of the houses around the harbour city"></div>
</main>

<footer>
<div class="abs tweet">
  <span class="dot"></span>
  <p>Check out 'QuellNest - Lorem Ipsum is simply dummy text of the printing and typesetting industry.<br>http://qn.example/x8Fa2Q</p>
</div>

<div class="abs footer">
  <h4 style="left:110px">RECENT NEWS</h4>
  <div class="news" style="top:112px"><div class="pic" role="img" aria-label="News thumbnail"></div><div><b>Lorem Ipsum is simply dummy text of the printing</b><small>Jan 12, 2019</small></div></div>
  <div class="news" style="top:207px"><div class="pic" role="img" aria-label="News thumbnail"></div><div><b>Lorem Ipsum is simply dummy text of the printing</b><small>Feb 03, 2019</small></div></div>

  <h4 style="left:363px">USEFUL LINKS</h4>
  <ul class="links" style="left:363px"><li>QuellNest</li><li>About Firm</li><li class="on">Mobile</li><li>Why us</li><li>Social Media</li><li>Site Map</li></ul>
  <ul class="links" style="left:496px"><li>Company</li><li>Latest Rooms</li><li>Tenants</li><li>Blog Posts</li><li>Help Topics</li><li>Policies</li></ul>

  <h4 style="left:611px">MAILING LIST</h4>
  <p class="mail-copy">Sign up for our mailing list to get latest updates and offers.</p>
  <div class="mail-field">Email Address</div>
  <div class="mail-btn"><svg width="12" height="12" viewBox="0 0 12 12"><path d="M2 6 5 9 10 3" fill="none" stroke="#fff" stroke-width="2"/></svg></div>
  <p class="privacy">We respect your privacy.</p>
  <span class="foot-social" style="left:617px"></span>
  <span class="foot-social" style="left:657px"></span>
  <span class="foot-social active" style="left:695px"></span>
  <span class="foot-social" style="left:733px"></span>
  <span class="foot-social" style="left:771px"></span>
  <span class="foot-social" style="left:809px"></span>

  <h4 style="left:861px">ABOUT FINANCE</h4>
  <p class="finance">Sed ut perspiciatis unde omnis iste natus error sit voluptatem accusantium doloremque laudantium</p>
  <div class="finance-row" style="top:190px"><svg viewBox="0 0 12 12"><rect x="0.5" y="2" width="11" height="8" fill="none" stroke="#888"/></svg><span>hello@quellnest.example</span></div>
  <div class="finance-row" style="top:222px"><svg viewBox="0 0 12 12"><rect x="3" y="0.5" width="6" height="11" rx="1" fill="none" stroke="#888"/></svg><span>P: 1234-4556-678</span></div>
  <div class="finance-row" style="top:256px"><svg viewBox="0 0 12 12"><path d="M6 11C2 6 2 5 2 4.5a4 4 0 0 1 8 0C10 5 10 6 6 11z" fill="none" stroke="#888"/></svg><span>12/6 Orrin St - Suite 204<br>United Kingdom - GA 30412</span></div>
</div>

<div class="abs bottom">
  <span class="copy">© QUELLNEST 2019</span>
  <div class="nav-links"><span>About</span><span>Services</span><span>Portfolio</span><span>Blog</span><span>Contact</span></div>
</div>
</footer>

</body>
</html>
```